Business Card Design Project

We need a business card design for an existing company in Dallas/Fort Worth that is expanding services and re-branding. We are changing the name from Brightmoor Commercial Cleaning to Keystride Facility Services. We are expanding from only commercial cleaning to include complete commercial landscape and facility maintenance services, too.

As stated, we offer a package of services that includes landscape, janitorial and facility services, which is largely unique in the industry.

We would like a design that communicates trust/partnership with a professional, corporate image, but not necessarily using the standard white business card. We would like a design that perhaps uses darker blues or perhaps a gray background, but we are open to other ideas. We might also be interested in a double-sided design - maybe with our logo on the back, printed on a gray background?

We will probably stick with the attached logo, but if you've got another inspired idea....

Target Market(s)

Property managers, commercial real estate professionals, corporate executives

Industry/Entity Type

Landscape

Requirements
Should not have
• Not interested in old style fonts.

```html
<!DOCTYPE html>
<html lang="en">
<head>
<meta charset="utf-8">
<title>Keystride Facility Services – Business Card</title>
<link rel="stylesheet" href="https://fonts.googleapis.com/css2?family=Questrial&family=Arimo:ital,wght@0,400;1,400&display=swap">
<style>
  :root {
    --ink: #000000;
    --paper: #ffffff;
    --card-glow: #3c3c3c;
    --card-edge: #050505;
    --text-light: #ffffff;
  }
  html, body {
    margin: 0;
    padding: 0;
    width: 1105px;
    height: 1200px;
    overflow: hidden;
    background: var(--ink);
  }
  .canvas {
    position: relative;
    width: 1105px;
    height: 1200px;
    background: var(--ink);
  }
  .sheet {
    position: absolute;
    left: 55px;
    top: 58px;
    width: 995px;
    height: 1079px;
    background: var(--paper);
  }
  .card {
    position: absolute;
    left: 125px;
    width: 832px;
    background: radial-gradient(ellipse at 50% 45%, var(--card-glow) 0%, #1a1a1a 45%, var(--card-edge) 80%);
    color: var(--text-light);
    overflow: hidden;
  }
  .card--front {
    top: 101px;
    height: 475px;
  }
  .card--back {
    top: 616px;
    height: 473px;
    background: var(--ink);
  }
  .brand-mark {
    position: absolute;
    left: 140px;
    top: 247px;
    width: 126px;
    height: 126px;
    border: 6px solid var(--text-light);
    box-sizing: border-box;
  }
  .card--front .brand-mark { left: 15px; top: 146px; }
  .brand-name {
    position: absolute;
    left: 167px;
    top: 92px;
    margin: 0;
    font-family: "Questrial", sans-serif;
    font-weight: 400;
    font-size: 80px;
    line-height: 1;
    letter-spacing: 12px;
    white-space: nowrap;
  }
  .brand-subname {
    position: absolute;
    left: 169px;
    top: 175px;
    margin: 0;
    font-family: "Questrial", sans-serif;
    font-weight: 400;
    font-size: 47px;
    line-height: 1;
    letter-spacing: 3.6px;
    white-space: nowrap;
  }
  .tagline {
    position: absolute;
    left: 169px;
    top: 266px;
    margin: 0;
    font-family: "Arimo", sans-serif;
    font-style: italic;
    font-size: 19.5px;
    line-height: 1;
    letter-spacing: 0.2px;
    white-space: nowrap;
  }
  .contact {
    position: absolute;
    left: 0;
    right: 0;
    top: 373px;
    margin: 0;
    text-align: center;
    font-family: "Arimo", sans-serif;
    font-size: 23px;
    line-height: 31px;
    font-style: normal;
  }
  .contact .sep { padding: 0 8px; }
  .back-frame {
    position: absolute;
    left: 12px;
    top: 12px;
    right: 12px;
    bottom: 12px;
    border: 13px solid var(--text-light);
    background: radial-gradient(ellipse at 50% 45%, var(--card-glow) 0%, #1a1a1a 45%, var(--card-edge) 85%);
  }
  .back-name {
    position: absolute;
    left: 0;
    right: 0;
    top: 50%;
    transform: translateY(-50%);
    margin: 0;
    text-align: center;
    font-family: "Questrial", sans-serif;
    font-weight: 400;
    font-size: 66px;
    letter-spacing: 10px;
    line-height: 1;
  }
</style>
</head>
<body>
<div class="canvas">
  <div class="sheet"></div>

  <section class="card card--front" aria-label="Card front">
    <div class="brand-mark" aria-hidden="true"></div>
    <h1 class="brand-name">KEYSTRIDE</h1>
    <h2 class="brand-subname">FACILITY SERVICES</h2>
    <p class="tagline">One Source For Landscape, Janitorial and Facility Maintenance</p>
    <address class="contact">
      Ridgeway 123<span class="sep">I</span>1234 Dallas, FW<span class="sep">I</span>T. 01 915 555 01 66<br>
      F. 555 01 67<span class="sep">I</span>E. info@keystridefs.com<span class="sep">I</span>www.keystridefs.com
    </address>
  </section>

  <section class="card card--back" aria-label="Card back">
    <div class="back-frame">
      <p class="back-name">KEYSTRIDE</p>
    </div>
  </section>
</div>
</body>
</html>
```